Letterhead Design Project

Attached is our new Logo and a copy of our old letter head
Looking to rebrand with our new logo

Reason: I want to show a business card design

Industry/Entity Type

Film Production

Colors

Designer to choose colors to be used in the design.

Requirements
Must have
• The information on the old letterhead

```html
<!DOCTYPE html>
<html lang="en">
<head>
<meta charset="utf-8">
<title>Kestrel International Letterhead</title>
<link rel="stylesheet" href="https://fonts.googleapis.com/css2?family=Russo+One&family=Quicksand:wght@500&family=Questrial&display=swap">
<style>
  :root {
    --brand-blue: #0a7faf;
    --brand-orange: #f07f22;
    --paper: #fdfdfd;
  }
  html, body {
    margin: 0;
    padding: 0;
    overflow: hidden;
    background: var(--paper);
  }
  .letterhead {
    position: relative;
    width: 1200px;
    height: 1200px;
    background: var(--paper);
    overflow: hidden;
  }
  .masthead {
    position: absolute;
    top: 36px;
    left: 290px;
    width: 594px;
    text-align: center;
  }
  .company-name {
    margin: 0;
    font-family: "Russo One", sans-serif;
    font-size: 60px;
    line-height: 1;
    letter-spacing: 1px;
    color: var(--brand-blue);
    white-space: nowrap;
  }
  .tagline {
    margin: 6px 0 0;
    font-family: "Quicksand", sans-serif;
    font-weight: 500;
    font-size: 24px;
    line-height: 1.1;
    color: var(--brand-orange);
    white-space: nowrap;
  }
  .divisions, .entity, .registration {
    margin: 0;
    font-family: "Questrial", sans-serif;
    color: var(--brand-blue);
    white-space: nowrap;
  }
  .divisions { font-size: 15.5px; margin-top: 2px; }
  .entity { font-size: 15px; margin-top: 2px; }
  .entity small { font-size: 9px; margin-right: 6px; }
  .registration { font-size: 12.5px; margin-top: 2px; }
  .footer-wave {
    position: absolute;
    left: 0;
    top: 0;
    width: 1200px;
    height: 1200px;
  }
  .wave-accent { fill: var(--brand-orange); }
  .wave-band { fill: var(--brand-blue); }
  .brand-seal {
    position: absolute;
    left: 42px;
    top: 975px;
    width: 120px;
    height: 120px;
    border-radius: 50%;
    background: #ffffff;
    box-shadow: 0 2px 6px rgba(0,0,0,0.15);
    display: flex;
    align-items: center;
    justify-content: center;
    font-family: "Questrial", sans-serif;
    font-size: 17px;
    letter-spacing: 1px;
    color: var(--brand-blue);
  }
  .contact {
    position: absolute;
    left: 34px;
    top: 1101px;
    font-family: "Questrial", sans-serif;
    font-size: 10px;
    line-height: 13px;
    color: var(--brand-blue);
  }
  .contact p { margin: 0; white-space: nowrap; }
  .contact .indent { padding-left: 16px; }
  .contact .reach { margin-top: 12px; padding-left: 26px; }
  .contact .reach p:first-child { padding-left: 8px; }
  .icon {
    width: 9px;
    height: 9px;
    vertical-align: -1px;
    margin-right: 3px;
    fill: var(--brand-blue);
  }
</style>
</head>
<body>
<div class="letterhead">
  <header class="masthead">
    <h1 class="company-name">KESTREL INTERNATIONAL</h1>
    <p class="tagline">Supply &amp; Management of Infrastructure &amp; Logistics</p>
    <p class="divisions">Kestrel Film Services&nbsp; Kestrel Pilot Escorts&nbsp; Kestrel Tour Management&nbsp; Kestrel Driver</p>
    <p class="entity"><small>Are Divisions Of</small>Kestrel International Pty Ltd</p>
    <p class="registration">Acn 482 617 305&nbsp; Abn 27 482 617 305</p>
  </header>

  <svg class="footer-wave" viewBox="0 0 1200 1200" aria-hidden="true">
    <path class="wave-accent" d="M0,1042 C300,1058 450,1120 760,1118 C960,1116 1100,1060 1200,1008 L1200,1126 C1100,1150 950,1165 820,1160 C500,1150 300,1095 0,1093 Z"/>
    <path class="wave-band" d="M0,1050 C300,1066 450,1128 760,1126 C960,1124 1100,1068 1200,1016 L1200,1126 C1100,1150 950,1165 820,1160 C500,1150 300,1095 0,1093 Z"/>
  </svg>

  <div class="brand-seal">KESTREL</div>

  <address class="contact">
    <p><svg class="icon" viewBox="0 0 10 10"><path d="M5 0a3.5 3.5 0 0 0-3.5 3.5C1.5 6 5 10 5 10s3.5-4 3.5-6.5A3.5 3.5 0 0 0 5 0zm0 5a1.4 1.4 0 1 1 0-2.8A1.4 1.4 0 0 1 5 5z"/></svg>P.O. Box 418 Marlow QLD 4310</p>
    <p class="indent">P.O.Box 732 Ferndale NSW 2175</p>
    <div class="reach">
      <p><svg class="icon" viewBox="0 0 10 10"><path d="M2.2 0.6l1.4 1.8-0.8 1.2c0.6 1.3 1.5 2.2 2.8 2.8l1.2-0.8 1.8 1.4-0.8 1.8C4.5 8.6 1.4 5.5 0.6 1.4z"/></svg>Ph. 0400 555 123</p>
      <p><svg class="icon" viewBox="0 0 10 10"><path d="M0 2h10v6H0z M0.6 2.4L5 5.6 9.4 2.4" stroke="#fff" stroke-width="0.8"/></svg>hello@kestrelintl.example</p>
    </div>
  </address>
</div>
</body>
</html>
```